Cellar Legacies, a definitive reference book on port

My husband has just finished writing a big book on Vintage Port. We need a hardcover book flap design for this book that is impressively huge. It's taken 10 years to research and write. It's 650 pages, interior is A4, exterior 4mm larger, and weighs nearly 3 kilos. It's a special book for people in the wine and port industry, as well as for someone who loves to drink Vintage Port. It can be a beautiful coffeetable book too.

The book is mainly about port and its declared vintages. It's also about the history of port, who drank it, when, how, where, who bought it, for how much, and the port houses are also described in detail.

The wine expert Gerald Thornwick wrote a book about vintage wine in 2002, and my husband would like to have a similar cover for his book. (A photo attached in files). I've attached other photos to give the designers an idea of the look and feel of the 'port culture', as well as photos of the typeface that my husband will be using for the inside hardcover.

Target Market(s)

Wine and port industry. Wine aficionados.

Industry/Entity Type

Winery

Font styles to use
Sans Serif
Script

Colors
ec1f27
1b1b1b
474747
333333
5c5c5c
faa54b

Requirements
Must have
• Book Cover must have Title: "Cellar Legacies" and "R. T. K. Hollister" (files attached to show proper typeface). One of the files is a flap jacket book cover that my husband designed himself. We're looking for more design ideas, and that pdf is a close winner to what he wants.
Nice to have
• illustration or painting of port glasses, or grapes, or similar. Dark colors, especially port wine, deep red wine colors. Gold writing, black writing, with red/berry/maroon accents. Luxury, elegance, has a masculine edge, traditional, but not too old-school and boring (like grandpa). Textures that are including with the culture of drinking vintage port are leather, velvet, cigar, wood, marble, winter, fireplaces. This sounds quite heavy, but it also should be simple and clean. I hope this isn't too confusing. Thanks!
Should not have
• Bright colors, playfulness.

```html
<!DOCTYPE html>
<html lang="en">
<head>
<meta charset="utf-8">
<title>Cellar Legacies – Book Jacket</title>
<link rel="stylesheet" href="https://fonts.googleapis.com/css2?family=Cinzel:wght@400;700;900&family=Open+Sans:wght@700&family=Yellowtail&display=swap">
<style>
  :root {
    --board: #333333;
    --spine: #1b1b1b;
    --spine-text: #474747;
    --ink: #1b1b1b;
    --gold: #faa54b;
    --port: #6e0f16;
    --port-deep: #3a070b;
  }
  * { margin: 0; padding: 0; box-sizing: border-box; }
  html, body { width: 1200px; height: 780px; overflow: hidden; background: var(--board); }
  .jacket {
    position: relative;
    width: 1200px;
    height: 780px;
    background: var(--board);
  }
  .back-cover {
    position: absolute; left: 0; top: 0;
    width: 549px; height: 780px;
    background: var(--board);
  }
  .spine {
    position: absolute; left: 549px; top: 0;
    width: 97px; height: 780px;
    background: var(--spine);
    display: flex; justify-content: center; align-items: flex-start;
    padding-top: 30px;
  }
  .spine-text {
    writing-mode: vertical-rl;
    font-family: "Open Sans", Arial, sans-serif;
    font-weight: 700;
    font-size: 34px;
    color: var(--spine-text);
    white-space: nowrap;
    line-height: 1;
  }
  .spine-title { text-transform: uppercase; margin-bottom: 40px; }
  .front-cover {
    position: absolute; left: 646px; top: 0;
    width: 554px; height: 780px;
    text-align: center;
  }
  .title {
    font-family: "Cinzel", Georgia, serif;
    font-weight: 900;
    color: var(--ink);
    text-transform: uppercase;
    line-height: 1;
    text-shadow: 2px 2px 0 var(--gold), 1px 1px 0 var(--gold);
    -webkit-text-stroke: 0.6px var(--gold);
  }
  .title-line-1 {
    position: absolute; left: 0; right: 0; top: 114px;
    font-size: 58px; letter-spacing: 3px;
  }
  .title-line-2 {
    position: absolute; left: 0; right: 0; top: 196px;
    font-size: 58px; letter-spacing: 4px;
  }
  .subtitle {
    position: absolute; left: 0; right: 0; top: 268px;
    font-family: "Cinzel", Georgia, serif;
    font-weight: 400;
    font-size: 17px;
    line-height: 19px;
    letter-spacing: 1px;
    color: var(--ink);
  }
  .artwork {
    position: absolute; left: 201px; top: 352px;
    width: 172px; height: 231px;
  }
  .author {
    position: absolute; left: 0; right: 0; top: 592px;
    font-family: "Yellowtail", cursive;
    font-size: 50px;
    color: var(--gold);
    line-height: 1.2;
  }
</style>
</head>
<body>
  <div class="jacket">
    <section class="back-cover"></section>

    <section class="spine">
      <div class="spine-text">
        <span class="spine-title">Cellar Legacies</span><span class="spine-author">R. T. K. Hollister</span>
      </div>
    </section>

    <section class="front-cover">
      <h1 class="title">
        <span class="title-line-1">Cellar</span>
        <span class="title-line-2">Legacies</span>
      </h1>
      <p class="subtitle">The Chronicle of Vintage Ports,<br>From the Beginning,<br>Substantiated and Comprehensive</p>
      <svg class="artwork" role="img" aria-label="Illustration of a port bottle, a filled wine glass, a cork and a bunch of dark grapes" viewBox="0 0 172 231">
        <defs>
          <linearGradient id="portTone" x1="0" y1="0" x2="0" y2="1">
            <stop offset="0" stop-color="#2a2a2a"/>
            <stop offset="0.5" stop-color="var(--port)"/>
            <stop offset="1" stop-color="var(--port-deep)"/>
          </linearGradient>
        </defs>
        <rect width="172" height="231" rx="6" fill="url(#portTone)"/>
      </svg>
      <p class="author">R. T. K. Hollister</p>
    </section>
  </div>
</body>
</html>
```